We are looking for a poster / flyer to advertise our Squash Tournament - the Wrenfold Club Sydney CBD Squash Open. I have provided the details and sponsor logos that need to appear on the poster in the attachments.
I am open to the poster including pictures of real life squash playing action shots or a complete graphic art design.

Target Market(s)

Squash Players and Sporty People who may be interested in trying Squash as a new Sport

Requirements
Must have
• 1. All logos attached in files (logos in the word doc and the Bramwick Logo)
2. Content that has been provided in the word doc
3. Printable on A3 paper
4. Title of the poster must be 2021 Wrenfold Club Sydney CBD Squash Open
Nice to have
• 1.Design must be related to the Sport of Squash (can either be a graphic Design that incorporates a real life squash pic rom the internet or 100% graphic)
2. Something incorporating both female and junior squash player participation.
3. Poster depicts action / athleticism.

```html
<!DOCTYPE html>
<html lang="en">
<head>
<meta charset="utf-8">
<title>2021 Wrenfold Club Sydney CBD Squash Open</title>
<link rel="stylesheet" href="https://fonts.googleapis.com/css2?family=Rubik+Distressed&family=Archivo:wght@400;600;700;800&family=Archivo+Narrow:wght@700&display=swap">
<style>
  :root {
    --stage: #e9e9e9;
    --paper: #f6f6f4;
    --paper-shade: #e7e7e4;
    --ink: #111111;
    --accent: #0d0d0d;
    --white: #ffffff;
    --photo-light: #eef2f3;
    --photo-skin: #d8b49a;
    --photo-court: #c9dde2;
  }
  * { margin: 0; padding: 0; box-sizing: border-box; }
  html, body {
    width: 1200px; height: 900px; overflow: hidden;
    background: var(--stage);
    font-family: "Archivo", Arial, sans-serif;
    color: var(--ink);
  }
  .poster {
    position: absolute; left: 297px; top: 20px;
    width: 606px; height: 860px;
    background: radial-gradient(ellipse at 50% 40%, var(--paper) 55%, var(--paper-shade) 100%);
    overflow: hidden;
    box-shadow: 0 4px 18px rgba(0,0,0,.18);
  }
  .abs { position: absolute; }

  .brand {
    left: 0; width: 100%; top: 16px; text-align: center;
    font-family: "Archivo", Arial, sans-serif; font-weight: 400;
    font-size: 31px; letter-spacing: 3px;
  }
  .brand-rule {
    left: 228px; width: 150px; top: 62px;
    border-top: 2px dotted var(--ink);
  }

  .year-tab {
    left: 34px; top: 88px; width: 40px; height: 88px;
    background: var(--accent); color: var(--white);
    display: flex; align-items: center; justify-content: center;
  }
  .year-tab span {
    transform: rotate(-90deg);
    font-family: "Archivo", Arial, sans-serif; font-weight: 800; font-size: 25px;
  }
  .title {
    left: 82px; top: 80px;
    font-family: "Rubik Distressed", Impact, sans-serif;
    font-size: 62px; line-height: 1; letter-spacing: 1px;
    color: var(--accent); text-transform: uppercase;
  }
  .subtitle {
    left: 84px; top: 148px;
    font-family: "Archivo Narrow", Arial, sans-serif; font-weight: 700;
    font-size: 23px;
  }

  .section-band { left: 0; top: 192px; width: 410px; height: 56px; }
  .section-band-label {
    left: 14px; top: 202px;
    font-family: "Archivo Narrow", Arial, sans-serif; font-weight: 700;
    font-size: 29px; color: var(--white); text-transform: uppercase;
  }

  .photo { border-radius: 4px; }
  .photo-player-female {
    left: 330px; top: 160px; width: 276px; height: 640px;
    background: linear-gradient(180deg, var(--photo-light) 0%, var(--photo-skin) 30%, var(--photo-light) 60%, var(--photo-court) 100%);
    opacity: .9;
  }
  .photo-players-male {
    left: 58px; top: 440px; width: 250px; height: 250px;
    background: linear-gradient(160deg, var(--photo-light) 0%, var(--photo-skin) 35%, #4d4d4d 70%, var(--photo-light) 100%);
    opacity: .85;
  }

  .details { left: 30px; top: 262px; width: 340px; list-style: none; }
  .details li {
    display: flex; gap: 10px; align-items: flex-start;
    font-weight: 600; font-size: 15px; line-height: 1.25; margin-bottom: 8px;
  }
  .details li.lead { font-size: 22px; font-weight: 700; margin-bottom: 10px; }
  .details svg { flex: none; margin-top: 3px; }

  .rule-dotted { left: 30px; width: 345px; border-top: 2px dotted var(--ink); }
  .bar-offer {
    left: 30px; top: 388px; width: 345px;
    font-weight: 700; font-size: 17px; line-height: 1.25;
  }

  .fee-badge {
    left: 290px; top: 516px; width: 136px; height: 136px; border-radius: 50%;
    background: var(--accent); color: var(--white);
    display: flex; flex-direction: column; align-items: center; justify-content: center;
  }
  .fee-badge .amount { font-weight: 800; font-size: 52px; line-height: .95; }
  .fee-badge .label { font-weight: 700; font-size: 16px; }

  .pill {
    left: 80px; top: 694px; width: 250px; height: 28px; border-radius: 14px;
    background: var(--accent); color: var(--white);
    font-family: "Archivo Narrow", Arial, sans-serif; font-weight: 700; font-size: 14px;
    display: flex; align-items: center; justify-content: center; text-transform: uppercase;
  }
  .mini-list { top: 730px; list-style: none; font-size: 8.5px; line-height: 1.35; font-weight: 600; }
  .mini-list.col-a { left: 50px; width: 150px; }
  .mini-list.col-b { left: 210px; width: 140px; border-left: 1px solid var(--ink); padding-left: 6px; }

  .contact-band { left: 0; top: 786px; width: 350px; height: 74px; }
  .contact-name {
    left: 30px; top: 800px; color: var(--white);
    font-family: "Archivo Narrow", Arial, sans-serif; font-weight: 700; font-size: 19px;
    display: flex; align-items: center; gap: 12px;
  }
  .contact-email {
    left: 30px; top: 830px; color: var(--white);
    font-size: 11px; letter-spacing: 2px;
  }

  .weekday-note {
    left: 368px; top: 782px; width: 220px;
    border-left: 5px solid var(--accent); padding-left: 8px;
    font-weight: 700; font-size: 12px; line-height: 1.2;
  }
  .entries-close {
    left: 381px; top: 834px;
    font-weight: 700; font-size: 11.5px;
  }
</style>
</head>
<body>
  <article class="poster">
    <div class="abs photo photo-player-female" role="img" aria-label="Action photo of a female squash player lunging for the ball on a bright court"></div>
    <div class="abs photo photo-players-male" role="img" aria-label="Photo of two male squash players in a rally"></div>

    <div class="abs brand">BRAMWICK</div>
    <div class="abs brand-rule"></div>

    <div class="abs year-tab"><span>2021</span></div>
    <h1 class="abs title">Wrenfold</h1>
    <p class="abs subtitle">Club Sydney CBD Squash Open</p>

    <svg class="abs section-band" viewBox="0 0 410 56" aria-hidden="true">
      <path d="M0 2 L380 0 L392 6 L384 12 L404 18 L396 26 L410 34 L392 40 L400 48 L372 54 L0 56 Z" fill="var(--accent)"/>
    </svg>
    <h2 class="abs section-band-label">Tournament Details</h2>

    <ul class="abs details">
      <li class="lead">
        <svg width="16" height="16" viewBox="0 0 16 16" aria-hidden="true"><circle cx="10" cy="6" r="4.5" fill="none" stroke="currentColor" stroke-width="1.6"/><path d="M7 9 L2 14" stroke="currentColor" stroke-width="2"/></svg>
        13 th – 15th August 2021
      </li>
      <li>
        <svg width="14" height="14" viewBox="0 0 16 16" aria-hidden="true"><circle cx="10" cy="6" r="4.5" fill="none" stroke="currentColor" stroke-width="1.6"/><path d="M7 9 L2 14" stroke="currentColor" stroke-width="2"/></svg>
        <span>Held at CBD Courts (Wrenfold &amp; Harlowe Clubs) and Eastgate Uni. Sports &amp; Fitness</span>
      </li>
      <li>
        <svg width="14" height="14" viewBox="0 0 16 16" aria-hidden="true"><circle cx="10" cy="6" r="4.5" fill="none" stroke="currentColor" stroke-width="1.6"/><path d="M7 9 L2 14" stroke="currentColor" stroke-width="2"/></svg>
        All finals will be at the Wrenfold Club
      </li>
    </ul>

    <div class="abs rule-dotted" style="top:380px"></div>
    <p class="abs bar-offer">Saturday Night Open Bar in CBD<br>provided by Sponsor ($3K bar tab)</p>
    <div class="abs rule-dotted" style="top:434px"></div>

    <div class="abs fee-badge"><span class="amount">$60</span><span class="label">ENTRY FEE</span></div>

    <div class="abs pill">Tournament Details</div>
    <ul class="abs mini-list col-a">
      <li>↗ Mens and Ladies Squash Open, $1k in prizemoney</li>
      <li>↗ Racquetball Open</li>
      <li>↗ Junior events</li>
    </ul>
    <ul class="abs mini-list col-b">
      <li>↗ All grades / abilities catered for</li>
      <li>↗ Players guaranteed 3 matches</li>
    </ul>

    <svg class="abs contact-band" viewBox="0 0 350 74" aria-hidden="true">
      <path d="M0 0 H318 L350 74 H0 Z" fill="var(--accent)"/>
    </svg>
    <div class="abs contact-name">
      <span>DANIEL FERROW</span>
      <svg width="14" height="16" viewBox="0 0 14 16" aria-hidden="true"><path d="M1 1 L13 8 L1 15 Z" fill="var(--white)"/></svg>
      <span>0491 570 166</span>
    </div>
    <div class="abs contact-email">Daniel.Ferrow@mailbox.net</div>

    <p class="abs weekday-note">Weekday matches also organised for CBD workers preferring to play during the day</p>
    <p class="abs entries-close">ENTRIES CLOSE 7TH AUGUST 2021</p>
  </article>
</body>
</html>
```